Business Cards and others
Business cards, stationery, Powerpoint template and E-mail Header and Footer
Professional
Darian Lutrell
CEO
4827 Thornwick Ln
Fenmoor MD 21093
darian@velmorix.com
www.velmorix.com

```html
<!DOCTYPE html>
<html lang="en">
<head>
<meta charset="utf-8">
<title>Velmorix Business Card</title>
<link href="https://fonts.googleapis.com/css2?family=Open+Sans:wght@400;600;700&display=swap" rel="stylesheet">
<style>
  :root {
    --page-bg: #e4e6e9;
    --brand-blue: #2a8fd0;
    --brand-blue-dark: #1673b4;
    --brand-blue-light: #5cb6ea;
    --band-pale: #cfe7f6;
    --card-white: #ffffff;
    --card-grey: #f1f2f4;
    --text-dark: #3a3f45;
    --text-muted: #6b7178;
    --divider: #c9d3db;
  }
  * { margin: 0; padding: 0; box-sizing: border-box; }
  html, body {
    width: 1200px; height: 901px; overflow: hidden;
    background: var(--page-bg);
    font-family: "Open Sans", Arial, sans-serif;
  }
  .canvas {
    width: 1200px; height: 901px;
    display: flex; flex-direction: column; align-items: center; justify-content: center;
    gap: 40px;
  }
  .card {
    position: relative;
    width: 700px; height: 400px;
    border-radius: 22px;
    overflow: hidden;
    box-shadow: 0 10px 30px rgba(0,0,0,0.18);
  }

  /* Back face */
  .card-back {
    background: linear-gradient(120deg, var(--brand-blue-light) 0%, var(--brand-blue) 55%, var(--brand-blue-dark) 100%);
  }
  .card-back .back-circle {
    position: absolute; left: -90px; top: 20px;
    width: 340px; height: 340px; border-radius: 50%;
    background: rgba(255,255,255,0.85);
  }
  .card-back .back-name {
    position: absolute; right: 48px; bottom: 60px;
    font-size: 58px; font-weight: 600; color: var(--card-white);
    letter-spacing: -0.5px;
  }

  /* Front face */
  .card-front {
    background: linear-gradient(180deg, var(--card-white) 0%, var(--card-grey) 100%);
  }
  .brand-block {
    position: absolute; left: 40px; top: 70px; width: 320px;
    display: flex; flex-direction: column; align-items: center;
  }
  .brand-mark {
    width: 96px; height: 96px; border-radius: 50%;
    background: linear-gradient(135deg, var(--brand-blue-light), var(--brand-blue-dark));
  }
  .brand-name {
    margin-top: 10px;
    font-size: 54px; font-weight: 600; color: var(--brand-blue);
    letter-spacing: -0.5px; line-height: 1;
  }
  .divider {
    position: absolute; left: 390px; top: 40px;
    width: 1px; height: 215px; background: var(--divider);
  }
  .contact {
    position: absolute; left: 412px; top: 40px;
    color: var(--text-dark); font-size: 13px; line-height: 1.45;
  }
  .contact .person-name {
    font-size: 24px; font-weight: 600; color: var(--brand-blue); line-height: 1.2;
  }
  .contact .person-role { font-size: 12px; color: var(--text-muted); margin-bottom: 22px; }
  .contact .address { margin-bottom: 10px; }
  .contact .line { display: flex; align-items: center; gap: 8px; }
  .contact .line svg { width: 13px; height: 13px; flex: none; }
  .band-pale {
    position: absolute; left: 0; right: 0; top: 276px; height: 66px;
    background: var(--band-pale);
  }
  .band {
    position: absolute; left: 0; right: 0; top: 286px; height: 46px;
    background: linear-gradient(90deg, var(--brand-blue-light), var(--brand-blue));
  }
  .website {
    position: absolute; left: 200px; top: 297px;
    color: var(--card-white); font-size: 16px; letter-spacing: 3px;
  }
  .corner-mark {
    position: absolute; right: 36px; top: 270px;
    width: 78px; height: 78px; border-radius: 50%;
    background: linear-gradient(135deg, var(--brand-blue-light), var(--brand-blue-dark));
    border: 4px solid var(--card-white);
  }
</style>
</head>
<body>
<main class="canvas">
  <section class="card card-back">
    <div class="back-circle"></div>
    <div class="back-name">Velmorix</div>
  </section>

  <section class="card card-front">
    <div class="brand-block">
      <div class="brand-mark"></div>
      <div class="brand-name">Velmorix</div>
    </div>
    <div class="divider"></div>
    <div class="contact">
      <div class="person-name">Darian Lutrell</div>
      <div class="person-role">CEO</div>
      <div class="address">4827 Thornwick Ln<br>Fenmoor MD 21093</div>
      <div class="line">
        <svg viewBox="0 0 16 16"><path d="M3 2h3l1 4-2 1c1 2 2 3 4 4l1-2 4 1v3c0 1-1 1-2 1C7 14 2 9 2 3c0-1 0-1 1-1z" fill="#3a3f45"/></svg>
        855-410-6397
      </div>
      <div class="line">
        <svg viewBox="0 0 16 16"><rect x="2" y="4" width="12" height="9" rx="1" fill="#3a3f45"/><rect x="5" y="2" width="6" height="3" fill="#3a3f45"/></svg>
        4435180276
      </div>
      <div class="line">
        <svg viewBox="0 0 16 16"><rect x="4" y="1" width="8" height="14" rx="1.5" fill="#3a3f45"/><rect x="5.5" y="3" width="5" height="8" fill="#fff"/></svg>
        9172054813
      </div>
      <div class="line">
        <svg viewBox="0 0 16 16"><rect x="1" y="3" width="14" height="10" rx="1" fill="#3a3f45"/><path d="M1.5 3.5 8 9l6.5-5.5" stroke="#fff" fill="none"/></svg>
        darian@velmorix.com
      </div>
    </div>
    <div class="band-pale"></div>
    <div class="band"></div>
    <div class="website">www.velmorix.com</div>
    <div class="corner-mark"></div>
  </section>
</main>
</body>
</html>
```